Motion Graphic (film) - Showreel NSA

Pixel Guild project- film
Nordic Screen Alliance
We deliver Digital Singage and sound solutions to retailers.
Our customers are retail chains in Sweden. Our main contacts are market managers and concept developers.
Main business is on delivering an improved customer experience through Digital Signage solutions and sound solutions for retail, public environment. We are a complete Digital Signage supplier with selected marketleading partners.
https://nordicscreenalliance.se/en/home/
https://nordicscreenalliance.se/en/gallery/
Project:
The task is to produce a film, Company Showreel on delivered customer solutions (installations) in two variants, one longer and one shorter for different purposes. One with a length of 1minute and a shorter version of about 20 seconds. From existing films on different installations, cut down and cut together with appropriate effects. The result should illustrate what NSA does and delivers to its customers.
Purpose:
The mission is to make a showreel/film to make us visible as an exhibitor at
the Shopfront Forum exhibition and arouse visitors' curiosity, i.e. draw visitors to our stand.
https://shopfrontforumevents.se/english/
The goal is for the film to be an eye-catcher where the visitor quickly understands what we deliver. There must be tempo and rhythm in the presentation. Texts are added that briefly explain the delivery. Will be sent when we have decided designer.
The showreel must be able to be shown on a 98" screen in 16:9 format.
The shorter version should be adapted for a header to our website.
Graphic expression:
The show reel must breathe NSA's graphic style, our high level of competence and our customer focus. Scripts will be added.
Fonts and logotype are enclosed.
Look and feel
Each slider illustrates characteristics of the customer's brand and the style your logo design should communicate.

```html
<!DOCTYPE html>
<html lang="en">
<head>
<meta charset="utf-8">
<title>Sound – Nordic Screen Alliance Showreel</title>
<link rel="stylesheet" href="https://fonts.googleapis.com/css2?family=Open+Sans:wght@600&display=swap">
<style>
  :root {
    --night: #03061a;
    --navy: #0b1850;
    --royal: #213f96;
    --haze: #5a6fb4;
    --speaker-blue: #2b64a3;
    --title-fill: rgba(72, 196, 192, 0.62);
    --title-stroke: #0b2a8c;
    --title-glow: rgba(79, 224, 216, 0.85);
    --level-white: #dcdde2;
    --level-blue: rgba(43, 110, 180, 0.85);
  }
  html, body {
    margin: 0;
    padding: 0;
    overflow: hidden;
    background: var(--night);
  }
  .frame {
    position: relative;
    width: 1200px;
    height: 649px;
    overflow: hidden;
    background: var(--night);
  }
  .mosaic-backdrop {
    position: absolute;
    inset: 0;
    background:
      radial-gradient(ellipse 30% 45% at 14% 60%, rgba(120, 135, 200, 0.55), transparent 70%),
      radial-gradient(ellipse 30% 30% at 70% 88%, rgba(90, 110, 190, 0.4), transparent 70%),
      radial-gradient(ellipse 25% 40% at 55% 45%, rgba(3, 6, 26, 0.7), transparent 70%),
      linear-gradient(90deg, var(--royal) 0%, var(--navy) 35%, var(--night) 60%, var(--navy) 85%, var(--night) 100%);
  }
  .speaker-icon {
    position: absolute;
    left: 0;
    top: 0;
    width: 310px;
    height: 280px;
  }
  .level-bar {
    position: absolute;
    width: 73px;
  }
  .level-bar--white {
    left: 934px;
    top: 23px;
    height: 496px;
    background: var(--level-white);
  }
  .level-bar--blue {
    left: 1025px;
    top: 325px;
    height: 197px;
    background: var(--level-blue);
  }
  .title {
    position: absolute;
    left: 0;
    top: 0;
    width: 1200px;
    height: 649px;
    margin: 0;
    z-index: 2;
  }
  .title-text {
    font-family: "Open Sans", "Verdana", sans-serif;
    font-weight: 600;
    font-size: 206px;
    fill: var(--title-fill);
    stroke: var(--title-stroke);
    stroke-width: 4px;
    filter: drop-shadow(0 0 5px var(--title-glow)) drop-shadow(0 0 12px var(--title-glow));
  }
</style>
</head>
<body>
  <main class="frame">
    <div class="mosaic-backdrop" role="img" aria-label="Pixel mosaic of blue and white data blocks on a dark background"></div>

    <svg class="speaker-icon" viewBox="0 0 310 280" aria-hidden="true">
      <path d="M103 62 L218 238 L64 268 L14 196 Z" fill="var(--speaker-blue)" stroke="var(--speaker-blue)" stroke-width="14" stroke-linejoin="round"/>
      <g fill="none" stroke="var(--speaker-blue)" stroke-width="18" stroke-linecap="round">
        <path d="M160 94 Q212 116 212 172"/>
        <path d="M166 54 Q250 84 254 184"/>
        <path d="M178 14 Q292 54 294 192"/>
      </g>
    </svg>

    <div class="level-bar level-bar--white"></div>
    <div class="level-bar level-bar--blue"></div>

    <svg class="title" viewBox="0 0 1200 649" role="heading" aria-level="1">
      <text class="title-text" x="264" y="368" textLength="670" lengthAdjust="spacingAndGlyphs">SOUND</text>
    </svg>
  </main>
</body>
</html>
```